Black Friday/Cyber Monday Sale

Email that will be go gout for our black friday/cyper Monday sale - will need 6 files. So it will be the design of the email and then 1 with the Birchwater Lodges logo, one with Meadow Falls logo, one with the Rewards logo, one with Velmora Logo, one with Fernhollow Inn logo and 1 with The Haven logo. I have attached a mock up but I am looking for something better

Target Market(s)

Email - previous and future guest

Industry/Entity Type

Hospitality

Requirements
Must have
• Black Friday Cyper Monday
• Save 19.68 on any 2019 stay when you book between November 21-26
• ____Near bottom___
• Celebrating the Past, Building the Future
• Since 1968 Birchwater Lodges has provided quality hospitality choices to the Smoky Mountain area. We've enjoyed sharing this year's 50th Anniversary with all of our guest and we look forward to seeing you all next year! We hope you'll take advantage of the last chance to save 19.68% this year when you book your 2019 stay between November 21st and 26th!
• *not valid in conjunction with any other offer, package, coupon, discount, online or group rate. Does not earn Birchwater Perks points. Minimum stay may be required. Other restrictions may apply.

```html
<!DOCTYPE html>
<html lang="en">
<head>
<meta charset="utf-8">
<title>Black Friday / Cyber Monday Sale</title>
<link rel="stylesheet" href="https://fonts.googleapis.com/css2?family=Lobster&family=Montserrat:wght@500&family=Raleway:wght@400;600&display=swap">
<style>
  :root {
    --board-light: #f2f2f2;
    --board-dark: #d6d6d6;
    --panel: #f6f2e7;
    --panel-low: #efe9db;
    --ink: #1b1b1b;
    --navy: #1d2350;
    --brown: #b8692f;
    --accent-orange: #e0701a;
    --rule: #d6857c;
    --caption: #111111;

    --green-dark: #3f8a1a;
    --green: #4eb01c;
    --green-deep: #2f6a18;

    --steel: #4f7a89;
    --gold: #d49a5a;
  }
  * { margin: 0; padding: 0; box-sizing: border-box; }
  html, body { width: 1200px; height: 871px; overflow: hidden; }
  body {
    background: radial-gradient(ellipse at 50% 45%, var(--board-light) 0%, var(--board-dark) 100%);
    position: relative;
    font-family: "Raleway", Arial, sans-serif;
    color: var(--ink);
  }

  .flyer {
    position: absolute;
    top: 58px;
    width: 502px;
    height: 707px;
    box-shadow: 0 6px 18px rgba(0,0,0,0.35);
  }
  .flyer--perks { left: 64px; --title: var(--green-dark); --headline: var(--green); --offer: var(--green-deep); --frame: var(--green); }
  .flyer--haven { left: 627px; --title: var(--steel); --headline: var(--gold); --offer: var(--steel); --frame: var(--steel); }

  .flyer__foliage {
    position: absolute; inset: 0;
    background:
      radial-gradient(circle at 12% 12%, #e6cf2a 0 14%, transparent 30%),
      radial-gradient(circle at 88% 8%, #c9cf3a 0 12%, transparent 28%),
      radial-gradient(circle at 8% 52%, #c4261c 0 14%, transparent 30%),
      radial-gradient(circle at 92% 60%, #e0a32a 0 12%, transparent 30%),
      radial-gradient(circle at 10% 92%, #e8952a 0 12%, transparent 28%),
      radial-gradient(circle at 90% 92%, #d9802a 0 12%, transparent 28%),
      linear-gradient(160deg, #b7471f 0%, #d89a2e 35%, #a8241c 65%, #c8742a 100%);
  }

  .flyer__panel {
    position: absolute;
    left: 38px; top: 37px;
    width: 424px; height: 630px;
    background: linear-gradient(to bottom, var(--panel) 0%, var(--panel) 74%, var(--panel-low) 100%);
    box-shadow: 0 2px 8px rgba(0,0,0,0.3);
  }

  .flyer__frame { position: absolute; left: 0; top: 0; width: 502px; height: 707px; pointer-events: none; }

  .brand {
    position: absolute;
    left: 0; right: 0; top: 50px; height: 74px;
    display: flex; align-items: center; justify-content: center;
  }
  .brand__name { font-family: "Lobster", cursive; font-size: 34px; color: var(--ink); }
  .brand--boxed .brand__box {
    width: 143px; height: 109px; background: #ffffff;
    display: flex; align-items: center; justify-content: center;
    margin-top: 36px;
  }
  .brand--boxed .brand__name { font-size: 28px; color: var(--steel); }

  .headline { position: absolute; left: 0; width: 502px; text-align: center; font-family: "Lobster", cursive; line-height: 1; }
  .headline--black-friday { top: 176px; font-size: 42px; color: var(--ink); }
  .headline--black-friday span { color: var(--title); }
  .headline--cyber { top: 222px; font-size: 72px; color: var(--headline); padding-left: 30px; }
  .headline--monday { top: 284px; font-size: 72px; color: var(--headline); padding-left: 44px; }

  .offer { position: absolute; left: 0; width: 502px; text-align: center; font-family: "Lobster", cursive; color: var(--offer); font-size: 22px; line-height: 27px; top: 437px; }

  .story { position: absolute; left: 0; width: 502px; text-align: center; font-family: "Lobster", cursive; line-height: 1; }
  .story--past { top: 515px; font-size: 21px; color: var(--brown); }
  .story--future { top: 539px; font-size: 29px; color: var(--navy); }

  .story__body {
    position: absolute; left: 67px; width: 368px; top: 579px;
    font-size: 9.6px; line-height: 12px; text-align: center; color: var(--ink);
  }
  .story__body strong { color: var(--accent-orange); font-weight: 600; }

  .divider { position: absolute; left: 224px; width: 53px; top: 658px; height: 2px; background: var(--rule); }

  .fine-print {
    position: absolute; left: 88px; width: 326px; top: 676px;
    font-size: 8.2px; line-height: 11px; text-align: center; color: var(--ink);
  }

  .caption {
    position: absolute; top: 798px; width: 560px;
    font-family: "Montserrat", Arial, sans-serif; font-weight: 500; font-size: 28px;
    color: var(--caption); text-align: center;
  }
  .caption--perks { left: 35px; }
  .caption--haven { left: 598px; }
</style>
</head>
<body>

<article class="flyer flyer--perks">
  <div class="flyer__foliage" role="img" aria-label="Border of colourful autumn leaves in yellow, red and orange"></div>
  <div class="flyer__panel"></div>
  <svg class="flyer__frame" viewBox="0 0 502 707" aria-hidden="true">
    <g stroke="var(--frame)" stroke-width="2.5" fill="none">
      <polyline points="142,120 112,120 112,318"/>
      <polyline points="360,120 390,120 390,353 134,353"/>
    </g>
  </svg>
  <div class="brand"><span class="brand__name">Birchwater Perks</span></div>
  <h1 class="headline headline--black-friday">Black <span>Friday</span></h1>
  <p class="headline headline--cyber">Cyper</p>
  <p class="headline headline--monday">Monday</p>
  <p class="offer">Save 19.68 on any 2019 stay<br>when you book between November 21-26</p>
  <p class="story story--past">Celebrating the Past,</p>
  <h2 class="story story--future">Building the Future</h2>
  <p class="story__body">Since 1968 Birchwater Lodges has provided quality hospitality choices to the Smoky Mountain area. We've enjoyed sharing this year's 50th Anniversary with all of our guest and we look forward to seeing you all next year! We hope you'll take advantage of the last chance to save 19.68% this year when you book your 2019 stay between <strong>November 21st and 26th!</strong></p>
  <div class="divider"></div>
  <p class="fine-print">*Not valid in conjunction with any other offer, package, coupon, discount, online or group rate. Does not earn Birchwater Perks points. Minimum stay may be required. Other restrictions may apply.</p>
</article>

<article class="flyer flyer--haven">
  <div class="flyer__foliage" role="img" aria-label="Border of colourful autumn leaves in yellow, red and orange"></div>
  <div class="flyer__panel"></div>
  <svg class="flyer__frame" viewBox="0 0 502 707" aria-hidden="true">
    <g stroke="var(--frame)" stroke-width="2.5" fill="none">
      <polyline points="175,120 112,120 112,318"/>
      <polyline points="330,120 390,120 390,353 134,353"/>
    </g>
  </svg>
  <div class="brand brand--boxed"><div class="brand__box"><span class="brand__name">The Haven</span></div></div>
  <h1 class="headline headline--black-friday">Black <span>Friday</span></h1>
  <p class="headline headline--cyber">Cyper</p>
  <p class="headline headline--monday">Monday</p>
  <p class="offer">Save 19.68 on any 2019 stay<br>when you book between November 21-26</p>
  <p class="story story--past">Celebrating the Past,</p>
  <h2 class="story story--future">Building the Future</h2>
  <p class="story__body">Since 1968 Birchwater Lodges has provided quality hospitality choices to the Smoky Mountain area. We've enjoyed sharing this year's 50th Anniversary with all of our guest and we look forward to seeing you all next year! We hope you'll take advantage of the last chance to save 19.68% this year when you book your 2019 stay between <strong>November 21st and 26th!</strong></p>
  <div class="divider"></div>
  <p class="fine-print">*Not valid in conjunction with any other offer, package, coupon, discount, online or group rate. Does not earn Birchwater Perks points. Minimum stay may be required. Other restrictions may apply.</p>
</article>

<p class="caption caption--perks">Black Friday/Cyber Monday Sale_1</p>
<p class="caption caption--haven">Black Friday/Cyber Monday Sale_2</p>

</body>
</html>
```